Two companies with one (great) goal... Need a Business card Design

Our Design consists of 2 companies with a common goal-- Embracing a Healthy Lifestyle!
1. The Vitality & Health Travel Trust- consists of a large ranch where horses, and crops of plants and vegetables are a significant component. Tourism developments are underway and the Ffoundation plays a significant role in supporting Sporting events.
2. Nuvacare is a manufacturer of medical and diagnostic equipment inclusive of small medical outposts throughout remote and rural regions of the country.

We are looking for a 2 sided business card with one company on each side. The ideal design will make the 2 different businesses flow together, while at the same time, also work if only one side was printed.

Information for Nuvacare Design:
Medical, Diagnostic and Laboratory Equipment | Medical Imaging Skyvault ScanHub | Biomedical Services
www.nuvacare.example
info@nuvacare.example
Tel: (389) 452) 1968

Information for The Vitality & Health Travel Trust:
DIRECTOR NAME
Belize, Central America
www.vitalitytrust.example
info@vitalitytrust.example
Tel: (507) 318-9275

*It is important that the font used is not too small please.

A few different color variations of each logo are included, any variation could be used.

Tagline is being finalized but ideally there would be a spot to add this in the future. Top tagline currently is "Healthy Lifestyle Through Better Living"

Industry/Entity Type

Medical

Requirements
Must have
• Font that is large enough to read

```html
<!DOCTYPE html>
<html lang="en">
<head>
<meta charset="utf-8">
<title>Nuvacare & The Vitality & Health Travel Trust – Business Cards</title>
<link href="https://fonts.googleapis.com/css2?family=Open+Sans:wght@400;600;700&display=swap" rel="stylesheet">
<style>
  :root {
    --page: #e9e7e3;
    --ink: #1c1c1c;
    --black-band: #0f1414;
    --silver-light: #f2f2f2;
    --silver-mid: #c9c9c9;
    --silver-dark: #8d8d8d;
    --gold-light: #f6ebc9;
    --gold-mid: #e2c57e;
    --gold-deep: #c9a24d;
    --white: #ffffff;
    --muted: #555555;
  }
  * { box-sizing: border-box; margin: 0; padding: 0; }
  html, body { width: 1200px; height: 800px; overflow: hidden; }
  body {
    background: var(--page);
    font-family: "Open Sans", Arial, sans-serif;
    color: var(--ink);
    position: relative;
  }
  .card {
    position: absolute;
    top: 250px;
    width: 520px;
    height: 300px;
    overflow: hidden;
    box-shadow: 0 6px 18px rgba(0,0,0,0.18);
  }

  /* ---------- Nuvacare side ---------- */
  .card--nuvacare { left: 50px; background: linear-gradient(180deg, var(--silver-light), var(--silver-mid) 70%, var(--silver-dark)); }
  .nuvacare__band {
    position: absolute; left: 0; top: 0; width: 100%; height: 118px;
    background: var(--black-band);
  }
  .nuvacare__brand {
    position: absolute; left: 30px; top: 28px;
    display: flex; align-items: center; gap: 14px;
    color: var(--white); font-weight: 600; font-size: 44px; letter-spacing: 4px;
    text-transform: uppercase;
  }
  .nuvacare__brand-square { width: 28px; height: 28px; background: var(--white); }
  .nuvacare__tagline-strip {
    position: absolute; left: 0; top: 118px; width: 100%; height: 28px;
    background: linear-gradient(90deg, var(--silver-dark), var(--silver-light) 30%, var(--silver-mid));
    border-top: 3px solid var(--white);
    display: flex; align-items: center; padding-left: 30px;
    font-size: 14px; color: var(--ink);
  }
  .nuvacare__services {
    position: absolute; left: 30px; top: 160px;
    list-style: none; font-size: 13px; line-height: 21px;
  }
  .nuvacare__services li::before {
    content: ""; display: inline-block; width: 6px; height: 6px; border-radius: 50%;
    background: var(--muted); margin-right: 8px; vertical-align: middle;
  }
  .nuvacare__contacts {
    position: absolute; left: 30px; top: 230px;
    list-style: none; font-size: 13px; line-height: 21px;
  }
  .nuvacare__flame {
    position: absolute; right: 0; top: 146px; width: 170px; height: 154px;
    background: linear-gradient(135deg, var(--silver-light), var(--silver-dark) 55%, var(--black-band));
  }

  /* ---------- Trust side ---------- */
  .card--trust { left: 630px; background: var(--white); }
  .trust__brand {
    position: absolute; right: 28px; top: 40px;
    display: flex; align-items: center; gap: 12px;
    font-size: 19px; font-weight: 600; letter-spacing: 1.5px; color: var(--ink);
    text-transform: uppercase; text-align: right;
  }
  .trust__brand-dot { width: 14px; height: 14px; border-radius: 50%; background: var(--gold-deep); }
  .trust__gold {
    position: absolute; left: 0; top: 92px; width: 340px; height: 208px;
    background: linear-gradient(90deg, var(--gold-light), var(--gold-mid) 70%, var(--gold-deep));
  }
  .trust__name { position: absolute; left: 26px; top: 104px; font-size: 19px; font-weight: 700; text-transform: uppercase; }
  .trust__title { position: absolute; left: 26px; top: 129px; font-size: 12px; color: var(--muted); }
  .trust__contacts {
    position: absolute; left: 26px; top: 160px;
    list-style: none; font-size: 14px; line-height: 24px;
  }
  .trust__location {
    position: absolute; left: 26px; top: 242px; font-size: 14px; line-height: 20px;
    display: flex; gap: 8px;
  }
  .trust__pattern {
    position: absolute; right: 26px; bottom: 22px; width: 150px; height: 120px;
    background: linear-gradient(135deg, var(--silver-mid), var(--gold-mid) 50%, var(--silver-dark));
  }

  .contact { display: flex; align-items: center; gap: 8px; }
  .icon { width: 14px; height: 14px; flex: none; }
</style>
</head>
<body>

<section class="card card--nuvacare" aria-label="Nuvacare business card">
  <div class="nuvacare__band">
    <div class="nuvacare__brand"><span>Nuvacare</span><span class="nuvacare__brand-square"></span></div>
  </div>
  <div class="nuvacare__tagline-strip">Healthy Lifestyle Through Better Living</div>
  <ul class="nuvacare__services">
    <li>Medical, Diagnostic and Laboratory Equipment</li>
    <li>Medical Imaging Skyvault ScanHub</li>
    <li>Biomedical Services</li>
  </ul>
  <ul class="nuvacare__contacts">
    <li class="contact">
      <svg class="icon" viewBox="0 0 14 14"><rect width="14" height="14" rx="2" fill="#555"/><path d="M4 3h2l1 2-1 1a5 5 0 0 0 2 2l1-1 2 1v2a1 1 0 0 1-1 1A7 7 0 0 1 3 4a1 1 0 0 1 1-1z" fill="#fff"/></svg>
      (389) 452) 1968</li>
    <li class="contact">
      <svg class="icon" viewBox="0 0 14 14"><rect width="14" height="14" rx="2" fill="#555"/><rect x="3" y="4" width="8" height="6" fill="none" stroke="#fff"/><path d="M3 4l4 3 4-3" fill="none" stroke="#fff"/></svg>
      info@nuvacare.example</li>
    <li class="contact">
      <svg class="icon" viewBox="0 0 14 14"><rect width="14" height="14" rx="2" fill="#555"/><circle cx="7" cy="7" r="4" fill="none" stroke="#fff"/><path d="M3 7h8M7 3v8" stroke="#fff"/></svg>
      www.nuvacare.example</li>
  </ul>
  <div class="nuvacare__flame" role="img" aria-label="Silver and black flame illustration"></div>
</section>

<section class="card card--trust" aria-label="The Vitality & Health Travel Trust business card">
  <div class="trust__brand"><span class="trust__brand-dot"></span><span>The Vitality &amp; Health<br>Travel Trust</span></div>
  <div class="trust__gold"></div>
  <p class="trust__name">Marcus Fenley</p>
  <p class="trust__title">Director</p>
  <ul class="trust__contacts">
    <li class="contact">
      <svg class="icon" viewBox="0 0 14 14"><rect width="14" height="14" rx="2" fill="#1c1c1c"/><path d="M4 3h2l1 2-1 1a5 5 0 0 0 2 2l1-1 2 1v2a1 1 0 0 1-1 1A7 7 0 0 1 3 4a1 1 0 0 1 1-1z" fill="#fff"/></svg>
      (507) 318-9275</li>
    <li class="contact">
      <svg class="icon" viewBox="0 0 14 14"><rect width="14" height="14" rx="2" fill="#1c1c1c"/><rect x="3" y="4" width="8" height="6" fill="none" stroke="#fff"/><path d="M3 4l4 3 4-3" fill="none" stroke="#fff"/></svg>
      info@vitalitytrust.example</li>
    <li class="contact">
      <svg class="icon" viewBox="0 0 14 14"><rect width="14" height="14" rx="2" fill="#1c1c1c"/><circle cx="7" cy="7" r="4" fill="none" stroke="#fff"/><path d="M3 7h8M7 3v8" stroke="#fff"/></svg>
      www.vitalitytrust.example</li>
  </ul>
  <div class="trust__location">
    <svg class="icon" viewBox="0 0 14 14"><rect width="14" height="14" rx="2" fill="#1c1c1c"/><path d="M7 2a3 3 0 0 1 3 3c0 2-3 6-3 6S4 7 4 5a3 3 0 0 1 3-3z" fill="#fff"/><circle cx="7" cy="5" r="1" fill="#1c1c1c"/></svg>
    <span>Belize<br>Central America</span>
  </div>
  <div class="trust__pattern" role="img" aria-label="Silver and gold checkered square pattern"></div>
</section>

</body>
</html>
```